Harbor Print Studio gallery website

I need a Website for a gallery with a shopify integration or maybe even better also compatible with squarespace.
the website should have following riders: Künstler, Veranstaltungen, Shop, About Us.
some nice examples for inspiration of the website architecture are:
https://www.tarnelgalerie.com/
https://www.mossline-gallery.com/de/
https://zinnbergalerie.de/
It should be easy for us to make adaptations and fill the website with new content.
Attached there is the CI an logo for the brand.
Art Collectors,
artgallery
3 page

```html
<!DOCTYPE html>
<html lang="en">
<head>
<meta charset="utf-8">
<title>Harbor Print Studio</title>
<link href="https://fonts.googleapis.com/css2?family=Italiana&family=Montserrat:wght@300;400;500;600&display=swap" rel="stylesheet">
<style>
:root{
  --green:#0b4540;
  --cream:#fdeddd;
  --red:#d8191a;
  --ink:#1d1d1d;
  --muted:#6f6f6f;
  --line:#cfcfcf;
  --white:#ffffff;
}
*{box-sizing:border-box;margin:0;padding:0}
html,body{width:1200px;height:5373px;overflow:hidden}
body{position:relative;background:var(--white);font-family:"Montserrat",sans-serif;color:var(--ink)}
.abs{position:absolute}
.display{font-family:"Italiana",serif;font-weight:400;letter-spacing:.18em;color:var(--ink);white-space:nowrap}
.fill{position:absolute}
/* header */
.site-header{left:0;top:0;width:1200px;height:134px;background:var(--white)}
.nav-link{position:absolute;top:65px;font-size:13px;letter-spacing:.06em;color:#333}
.brand{position:absolute;left:450px;top:14px;width:300px;text-align:center}
.brand-mark{display:block;width:30px;height:30px;border:1.5px solid var(--red);margin:0 auto 20px}
.brand-name{font-size:17px;font-weight:400;color:#333;letter-spacing:.02em;white-space:nowrap}
/* hero */
.hero{left:0;top:134px;width:1200px;height:550px;background:linear-gradient(120deg,#2f6aa8 0%,#5bb3c2 18%,#f08a24 38%,#e94b3a 52%,#8b3fb0 70%,#f5b23c 88%,#3f8fd0 100%)}
.hero-caption{left:0;top:511px;width:468px;height:111px;background:rgba(110,110,100,.72)}
.hero-caption .bar{position:absolute;left:30px;top:18px;width:2px;height:75px;background:rgba(255,255,255,.7)}
.hero-caption h2{position:absolute;left:53px;top:28px;font-weight:400;font-size:24px;letter-spacing:.06em;color:var(--white);white-space:nowrap}
.hero-caption p{position:absolute;left:53px;top:68px;font-size:14px;color:#eee}
.arrow-btn{position:absolute;background:var(--red);display:flex;align-items:center;justify-content:center}
/* gallery */
.section-title{font-size:46px}
.btn{position:absolute;background:var(--red);color:var(--white);font-size:15px;display:flex;align-items:center;justify-content:center}
.card{position:absolute;top:879px;width:273px;height:440px;background:var(--white);box-shadow:0 2px 10px rgba(0,0,0,.1);overflow:hidden}
.card .pic{position:absolute;left:12px;top:14px;width:249px;height:290px}
.card .artist{position:absolute;left:12px;top:326px;font-size:13px;color:var(--muted)}
.card .name{position:absolute;left:12px;top:350px;font-size:17px;letter-spacing:.05em;font-weight:500;white-space:nowrap}
.card .kind{position:absolute;left:12px;top:384px;font-size:11px;color:var(--muted)}
.card .more{position:absolute;left:12px;top:404px;font-size:13px;color:var(--red);text-decoration:underline}
.circle-btn{position:absolute;width:38px;height:38px;border-radius:50%;border:1.5px solid var(--ink);display:flex;align-items:center;justify-content:center}
/* about */
.about{left:0;top:1528px;width:1200px;height:444px}
.body-text{font-size:12px;line-height:20px;color:#444}
/* category */
.cat{position:absolute;overflow:hidden}
.cat::after{content:"";position:absolute;left:0;right:0;bottom:0;height:45%;background:linear-gradient(transparent,rgba(0,0,0,.55))}
.cat span{position:absolute;left:28px;bottom:28px;color:var(--white);font-size:18px;letter-spacing:.08em;font-weight:500;z-index:1}
/* form */
.field{position:absolute;border:1px solid #bbb;font-size:12px;color:#777;padding:16px 15px}
/* footer */
.footer{left:0;top:5000px;width:1200px;height:373px;background:var(--green);color:#d9e4e2}
.foot-col{position:absolute;top:90px}
.foot-col h4{font-weight:400;font-size:14px;margin-bottom:18px;color:var(--white)}
.foot-col a{display:block;font-size:12px;color:#c5d4d1;line-height:23px;text-decoration:none}
</style>
</head>
<body>

<header class="abs site-header">
  <span class="nav-link" style="left:140px">KÜNSTLER</span>
  <span class="nav-link" style="left:270px">VERANSTALTUNGEN</span>
  <div class="brand"><span class="brand-mark"></span><span class="brand-name">HARBOR PRINT STUDIO</span></div>
  <span class="nav-link" style="left:818px">ABOUT US</span>
  <span class="nav-link" style="left:930px">SHOP</span>
  <svg class="abs" style="left:1036px;top:62px" width="18" height="18" viewBox="0 0 18 18"><circle cx="7.5" cy="7.5" r="5.5" fill="none" stroke="#333" stroke-width="1.5"/><line x1="11.5" y1="11.5" x2="16" y2="16" stroke="#333" stroke-width="1.5"/></svg>
  <svg class="abs" style="left:1066px;top:62px" width="20" height="18" viewBox="0 0 20 18"><path d="M10 16 C3 11 1 8 1 5.5 A4.5 4.5 0 0 1 10 4 A4.5 4.5 0 0 1 19 5.5 C19 8 17 11 10 16Z" fill="none" stroke="#333" stroke-width="1.5"/></svg>
</header>

<section class="abs hero" role="img" aria-label="Colourful textured painting of a large eye"></section>
<div class="abs hero-caption">
  <span class="bar"></span>
  <h2>GAZE OF THE INFINITE</h2>
  <p>Mira Holloway</p>
  <div class="arrow-btn" style="left:396px;top:40px;width:40px;height:36px">
    <svg width="18" height="14" viewBox="0 0 18 14"><path d="M1 7H16M10 1l6 6-6 6" fill="none" stroke="#fff" stroke-width="1.8"/></svg>
  </div>
</div>

<section class="gallery">
  <h2 class="abs display section-title" style="left:138px;top:760px">GALLERY</h2>
  <p class="abs" style="left:140px;top:828px;font-size:14px;color:#444">Reesizing move editor bullet pencil</p>
  <a class="btn" style="left:933px;top:795px;width:125px;height:40px">View All</a>

  <article class="card" style="left:140px">
    <div class="pic" role="img" aria-label="Collage artwork of a sculpture bust on yellow stripes" style="background:linear-gradient(135deg,#f3c431 0 55%,#1f8a8a 56% 80%,#e5533a 81%)"></div>
    <span class="artist">Jonas Vell</span><span class="name">IRIDESCENT INSIGHT</span><span class="kind">Painting</span><span class="more">Learn more →</span>
  </article>
  <article class="card" style="left:440px">
    <div class="pic" role="img" aria-label="Abstract painting in violet and turquoise" style="background:linear-gradient(100deg,#6b3fb2,#c79ad8 30%,#5fc7d9 55%,#b06cc9 80%,#7a3fae)"></div>
    <span class="artist">Jonas Vell</span><span class="name">IRIDESCENT INSIGHT</span><span class="kind">Painting</span><span class="more">Learn more →</span>
  </article>
  <article class="card" style="left:740px">
    <div class="pic" role="img" aria-label="Monochrome portrait collage with flowers" style="background:linear-gradient(160deg,#e08a4c 0 18%,#bdb7ad 19% 60%,#7d7a74)"></div>
    <span class="artist">Jonas Vell</span><span class="name">IRIDESCENT INSIGHT</span><span class="kind">Painting</span><span class="more">Learn more →</span>
  </article>
  <article class="card" style="left:1040px">
    <div class="pic" role="img" aria-label="Classical painting of two figures" style="background:linear-gradient(135deg,#f6dcd8,#e9b9a4 50%,#f5e3de)"></div>
    <span class="artist">Jonas Vell</span><span class="name">IRIDESCENT INSIGHT</span><span class="kind">Painting</span><span class="more">Learn more →</span>
  </article>

  <div class="abs" style="left:140px;top:1381px;width:793px;height:1px;background:var(--line)"></div>
  <div class="abs" style="left:140px;top:1380px;width:264px;height:3px;background:var(--ink)"></div>
  <div class="circle-btn" style="left:964px;top:1363px;border-color:#bbb"><svg width="10" height="14" viewBox="0 0 10 14"><path d="M8 1 2 7l6 6" fill="none" stroke="#bbb" stroke-width="1.6"/></svg></div>
  <div class="circle-btn" style="left:1018px;top:1363px"><svg width="10" height="14" viewBox="0 0 10 14"><path d="M2 1l6 6-6 6" fill="none" stroke="#1d1d1d" stroke-width="1.6"/></svg></div>
</section>

<section class="abs about">
  <div class="fill" style="left:0;top:0;width:600px;height:444px;background:var(--green)"></div>
  <div class="fill" style="left:600px;top:0;width:600px;height:444px;background:var(--cream)"></div>
  <div class="fill" style="left:71px;top:48px;width:461px;height:354px;background:#c9a976;padding:12px">
    <div role="img" aria-label="Surreal painting with a white horse and umbrella" style="width:100%;height:100%;background:linear-gradient(135deg,#e9ece2,#b9c2b0 50%,#7c8a6e)"></div>
  </div>
  <h2 class="abs display section-title" style="left:684px;top:58px">ABOUT US</h2>
  <p class="abs body-text" style="left:684px;top:138px;width:380px">Figma ipsum component variant main layer. Reesizing move editor bullet pencil. Connection draft arrow project align background component line. Opacity thumbnail team scale vertical figma stroke distribute vector. Frame scale boolean community object italic.</p>
  <p class="abs body-text" style="left:684px;top:248px;width:380px">Opacity thumbnail team scale vertical figma stroke distribute vector. Frame scale boolean community object italic.</p>
  <a class="btn" style="left:684px;top:344px;width:151px;height:42px">Read More</a>
</section>

<section class="category">
  <h2 class="abs display section-title" style="left:0;width:1200px;text-align:center;top:2098px">BY CATEGORY</h2>
  <div class="cat" style="left:140px;top:2191px;width:294px;height:608px;background:linear-gradient(160deg,#f3c534 0 35%,#8f9bdc 36% 55%,#6b6b6b 56% 75%,#2f6e4f)" role="img" aria-label="Collage of a sculpted torso with red lips"><span>PAINTING</span></div>
  <div class="cat" style="left:451px;top:2191px;width:294px;height:295px;background:linear-gradient(135deg,#3b6fc2,#e4a74b 50%,#7a4fb0)" role="img" aria-label="Painted hands holding a camera"><span>PHOTOGRAPHY</span></div>
  <div class="cat" style="left:764px;top:2191px;width:294px;height:295px;background:linear-gradient(135deg,#e9e4dc,#8cbcc0 50%,#4e5a52)" role="img" aria-label="Collage of an eye among leaves"><span>WORK ON PAPER</span></div>
  <div class="cat" style="left:451px;top:2504px;width:294px;height:295px;background:linear-gradient(160deg,#c9c1c4,#d889c8 50%,#5d8fcf)" role="img" aria-label="Colourful sculpture of a bearded head"><span>SCULPTURE</span></div>
  <div class="cat" style="left:764px;top:2504px;width:294px;height:295px;background:linear-gradient(135deg,#f3f0ec 0 50%,#e6a3a3 51% 70%,#2f3b46)" role="img" aria-label="Print with an arch and botanical shapes"><span>PRINTMAKING</span></div>
</section>

<section class="abs" style="left:0;top:2924px;width:1200px;height:492px;background:var(--cream)">
  <p class="abs" style="left:140px;top:122px;font-size:15px">Artist</p>
  <h2 class="abs display" style="left:138px;top:146px;font-size:42px">MIRA HOLLOWAY</h2>
  <p class="abs body-text" style="left:140px;top:217px;width:390px">Figma ipsum component variant main layer. Reesizing move editor bullet pencil. Connection draft arrow project align background component line. Opacity thumbnail team scale vertical figma stroke distribute vector. Frame scale boolean community object italic.</p>
  <p class="abs body-text" style="left:140px;top:330px;width:390px">Opacity thumbnail team scale vertical figma stroke distribute vector. Frame scale boolean community object italic.</p>
  <div class="abs" style="left:814px;top:39px;width:234px;height:224px;border:2px solid var(--red)"></div>
  <div class="abs" style="left:998px;top:53px;width:89px;height:210px;border:2px solid var(--red)"></div>
  <div class="abs" role="img" aria-label="Portrait of the artist seated in front of a painting" style="left:680px;top:62px;width:361px;height:382px;background:linear-gradient(160deg,#d86a2c,#3f5a7a 40%,#8a7f72 70%,#2b2b2b)"></div>
  <div class="arrow-btn" style="left:680px;top:392px;width:98px;height:52px">
    <svg width="46" height="14" viewBox="0 0 46 14"><path d="M17 7H2M7 2 2 7l5 5M29 7h15M39 2l5 5-5 5" fill="none" stroke="#fff" stroke-width="1.6"/></svg>
  </div>
</section>

<section class="abs" style="left:0;top:3416px;width:1200px;height:468px;background:var(--green);color:var(--white)">
  <h2 class="abs display section-title" style="left:0;width:1200px;text-align:center;top:66px;color:var(--white)">REVIEW</h2>
  <div class="abs" role="img" aria-label="Reviewer avatar" style="left:566px;top:155px;width:66px;height:66px;border-radius:50%;border:2px solid #fff;background:linear-gradient(160deg,#c87a4a,#5a4a40)"></div>
  <p class="abs" style="left:310px;top:248px;width:580px;text-align:center;font-size:14px;line-height:24px;color:#dfe8e6">Figma ipsum component variant main layer. Reesizing move editor bullet pencil. Connection draft arrow project align background component line. Opacity thumbnail team scale vertical figma stroke distribute vector. Frame scale boolean community object italic.</p>
  <div class="circle-btn" style="left:225px;top:267px;border-color:#6f8f8b"><svg width="10" height="14" viewBox="0 0 10 14"><path d="M8 1 2 7l6 6" fill="none" stroke="#6f8f8b" stroke-width="1.6"/></svg></div>
  <div class="circle-btn" style="left:933px;top:267px;border-color:#fff"><svg width="10" height="14" viewBox="0 0 10 14"><path d="M2 1l6 6-6 6" fill="none" stroke="#fff" stroke-width="1.6"/></svg></div>
  <p class="abs" style="left:0;width:1200px;text-align:center;top:358px;font-size:16px">Mira Holloway</p>
  <p class="abs" style="left:0;width:1200px;text-align:center;top:384px;font-size:16px;color:#f2c230;letter-spacing:3px">★★★★★</p>
</section>

<section class="abs" style="left:0;top:3884px;width:1200px;height:488px;background:var(--cream)">
  <div class="abs" role="img" aria-label="Portrait collage with white lilies and plants" style="left:0;top:0;width:526px;height:488px;background:linear-gradient(150deg,#e8dfd4,#e39b6a 45%,#5b88a8 75%,#2c4e63)"></div>
  <p class="abs" style="left:599px;top:89px;font-size:17px;color:var(--red)">Next Event</p>
  <h2 class="abs display" style="left:599px;top:120px;font-size:36px;line-height:46px">A SHOWCASE OF<br>TIMELESS ELEGANCE</h2>
  <svg class="abs" style="left:599px;top:226px" width="16" height="16" viewBox="0 0 16 16"><rect x="1.5" y="3" width="13" height="11.5" fill="none" stroke="#d8191a" stroke-width="1.3"/><line x1="1.5" y1="7" x2="14.5" y2="7" stroke="#d8191a" stroke-width="1.3"/><line x1="5" y1="1" x2="5" y2="4.5" stroke="#d8191a" stroke-width="1.3"/><line x1="11" y1="1" x2="11" y2="4.5" stroke="#d8191a" stroke-width="1.3"/></svg>
  <p class="abs" style="left:622px;top:225px;font-size:14px">March 15th, 2024</p>
  <p class="abs" style="left:599px;top:268px;width:450px;font-size:14px;line-height:23px;color:#444">Join us at Harbor Print Studio for an exquisite evening of artistic splendor as we unveil our latest collection, "Artistry Unveiled."</p>
  <a class="btn" style="left:599px;top:380px;width:209px;height:47px;font-size:17px">Register Now</a>
</section>

<section class="contact">
  <h2 class="abs display section-title" style="left:0;width:1200px;text-align:center;top:4474px">CONTACT US</h2>
  <p class="abs" style="left:330px;top:4548px;width:540px;text-align:center;font-size:14px;line-height:23px;color:#444">Opacity thumbnail team scale vertical figma Opacity thumbnail team scale vertical figma</p>
  <div class="field" style="left:255px;top:4623px;width:336px;height:46px">Full name</div>
  <div class="field" style="left:607px;top:4623px;width:336px;height:46px">Phone number</div>
  <div class="field" style="left:255px;top:4687px;width:688px;height:46px">Email address</div>
  <div class="field" style="left:255px;top:4750px;width:688px;height:105px">Your message...</div>
  <a class="btn" style="left:538px;top:4886px;width:122px;height:41px">Submit</a>
</section>

<footer class="abs footer">
  <div class="abs" style="left:95px;top:80px;width:240px;text-align:center">
    <span style="display:block;width:30px;height:30px;border:1.5px solid #9fb7b3;margin:0 auto 14px"></span>
    <span style="font-size:16px;color:#e6eeec;white-space:nowrap">HARBOR PRINT STUDIO</span>
    <div style="margin-top:26px;display:flex;justify-content:center;gap:10px">
      <span style="width:20px;height:20px;border-radius:50%;border:1px solid #9fb7b3"></span>
      <span style="width:20px;height:20px;border-radius:50%;border:1px solid #9fb7b3"></span>
      <span style="width:20px;height:20px;border-radius:50%;border:1px solid #9fb7b3"></span>
    </div>
  </div>
  <div class="abs" style="left:420px;top:88px;width:1px;height:150px;background:#2f6560"></div>
  <div class="abs" style="left:620px;top:88px;width:1px;height:150px;background:#2f6560"></div>
  <div class="abs" style="left:820px;top:88px;width:1px;height:150px;background:#2f6560"></div>
  <div class="foot-col" style="left:447px"><h4>QUICK LINKS</h4><a>Künstler</a><a>About Us</a><a>Veranstaltungen</a><a>Shop</a><a>Contact Us</a></div>
  <div class="foot-col" style="left:647px"><h4>BY CATEGORY</h4><a>Painting</a><a>Photography</a><a>Sculpture</a><a>Work on Paper</a><a>Printmaking</a></div>
  <div class="foot-col" style="left:847px"><h4>LEGAL</h4><a>Privacy Policy</a><a>Terms and Conditions</a><a>Site Map</a></div>
  <p class="abs" style="left:0;width:1200px;text-align:center;top:304px;font-size:12px;color:#c5d4d1">© 2024 All Rights Reserved | Harbor Print Studio</p>
</footer>

</body>
</html>
```